Website Design for a chemical distribution company

Designer must provide full implementation/coding depending on the platform chosen by the client we'd prefer wordpress type CMS system.

We need a modern and bold website setup for our chemical distribution company. It will need to be like a web store however, no purchases take place on the website only inquiries. So for example the customer can go to a product and click on a button that brings up an inquiry window, they populate that with their information and it sends me an email with the inquiry.

We need it done 3 times pretty much the same but maybe a different colour scheme for each industry. for example on the welcome screen we want 3 icons /pictures ie: plastic, resin, industrial. When the customer clicks on the industry they need it directs them to the specific area that is perhaps on a subdomain or somewhere on the main domain but with no relation to the other industries I hope this makes sense. The layout would be the same but their should be some difference such as colours etc.

The site needs to have a powerful search engine that is very accurate.

It will have about 40,000 products and needs to be able to upload our products via an excel spreed sheet.

We need it to look graphically amazing and very easy to use for the customer.

It will also need to have a blog section that we can upload blogs to daily with different sub categories for things such as experiments, news etc.

The front page needs to be have a banner/advertisement window that is easy for us to change with new specials/deals that we bring out.

Basically the site needs to be easy to navigate, easy to get to products and inquire and needs to have a wow factor.

We also need a special requess page that gives the customers the facility to request a product that they can't find on our website.

I need to stress the importance of a search engine on the site that can handle searching through all the products.

We will also give you the words and you will need to put those on to the pages.

You will also be required to upload our catalogue via CSV or Excel to the site on final completion.

Please find similar websites below for companies that similar to us:

www.tarbexo.com
www.kovrel-dunmark.com
http://www.lumbridlab.com.au
Updates

Just to clarify only one of the websites will have 40-50k products the other 2 industries will only have about 200-500 products each. Added Sunday, February 14, 2016

Target Market(s)

Chemicals, Food, Pharmaceuticals, Business to Business

Industry/Entity Type

It Company

Coding

Coded - Design and coding required

Number of Pages Required

5+ page

Font styles to use
Sans Serif

Requirements
Must have
• Powerful search engine
• Great design
• Easy to use CMS
• SEO
• Mobile Device Compatible

```html
<!DOCTYPE html>
<html lang="en">
<head>
<meta charset="utf-8">
<title>Norvane — Chemical Distribution</title>
<link rel="stylesheet" href="https://fonts.googleapis.com/css2?family=Open+Sans:wght@300;400;600;700&family=Raleway:wght@400;500;600&display=swap">
<style>
:root{
  --blue:#0b78c4;
  --blue-deep:#06518a;
  --blue-dark:#0a4f86;
  --dark:#3d3d3d;
  --panel:#444;
  --ink:#333;
  --muted:#555;
  --line:#d8d8d8;
  --white:#fff;
}
*{margin:0;padding:0;box-sizing:border-box}
html,body{width:754px;height:1200px;overflow:hidden;background:var(--white)}
body{font-family:"Open Sans",Arial,sans-serif;color:var(--ink)}
.page{position:absolute;left:0;top:0;width:1350px;height:2149px;transform:scale(.55852);transform-origin:0 0}
.abs{position:absolute}
.heading-font{font-family:"Raleway","Open Sans",sans-serif}

/* header */
.brand{left:100px;top:12px;display:flex;align-items:center;gap:10px}
.brand-dot{width:22px;height:22px;border-radius:50%;background:var(--blue)}
.brand-name{font-size:32px;font-weight:700;color:var(--blue)}
.contact-item{display:flex;align-items:center;gap:12px}
.contact-label{font-size:12px;color:var(--muted);line-height:16px}
.contact-value{font-size:14px;color:var(--ink)}
.contact-value.phone{font-size:16px;color:var(--blue)}

/* nav */
.nav{left:0;top:68px;width:1350px;height:54px;background:var(--dark)}
.nav-item{top:0;height:54px;line-height:56px;font-size:14px;color:var(--white)}
.nav-item.active{background:var(--blue);width:88px;text-align:center;left:100px}
.search-sep{left:1032px;top:16px;width:1px;height:22px;background:#666}
.search-text{left:1049px;top:16px;font-size:14px;color:#bbb}

/* hero */
.hero{left:0;top:122px;width:1350px;height:582px;overflow:hidden;
  background:linear-gradient(180deg,#6fa7db 0%,#a9c7e3 40%,#c9d3db 70%,#8fa3b5 100%)}
.hero-title{left:100px;top:190px;font-size:51px;font-weight:600;color:var(--white);white-space:nowrap}
.hero-text{left:101px;top:257px;width:590px;font-size:16px;line-height:27px;color:var(--white)}
.btn-more{left:100px;top:329px;width:150px;height:49px;border-radius:25px;background:var(--dark);color:var(--white);font-size:15px;text-align:center;line-height:49px}
.request{left:867px;top:68px;width:383px;height:435px;background:var(--panel);border-top:4px solid var(--blue)}
.request-title{left:0;top:24px;width:100%;text-align:center;font-size:24px;font-weight:600;color:var(--white);letter-spacing:.3px}
.field{left:21px;width:337px;background:var(--white);border-radius:2px;font-size:14px;color:#555;padding:15px 20px}
.submit{left:21px;top:363px;width:337px;height:50px;background:var(--blue);color:var(--white);font-weight:700;font-size:16px;text-align:center;line-height:50px}
.dot{top:537px;width:12px;height:12px;border-radius:50%;border:2px solid var(--white)}
.dot.on{background:var(--white)}

/* section headings */
.section-title{left:0;width:1350px;text-align:center;font-size:34px;color:var(--ink)}
.rule{height:1px;background:var(--line)}
.rule-accent{height:3px;background:var(--blue)}

/* categories */
.category{top:823px;width:370px;height:278px;overflow:hidden}
.category-photo{position:absolute;inset:0}
.category-band{position:absolute;left:0;bottom:0;width:100%;height:55px;background:rgba(61,61,61,.85)}
.category.resin .category-band{background:var(--blue)}
.category-badge{position:absolute;left:145px;top:182px;width:80px;height:80px;border-radius:50%;background:rgba(61,61,61,.85)}
.category.resin .category-badge{background:var(--blue)}
.category-label{position:absolute;left:0;bottom:15px;width:100%;text-align:center;font-size:17px;color:var(--white)}

/* blog */
.post-photo{top:1249px;width:250px;height:248px}
.post-card{top:1232px;width:304px;height:281px;border:1px solid var(--line);background:var(--white)}
.post-title{left:33px;top:42px;font-size:19px;color:var(--ink)}
.post-mark{left:33px;top:70px;width:13px;height:2px;background:var(--blue)}
.post-text{left:34px;top:86px;width:250px;font-size:12px;line-height:20.4px;color:var(--muted);max-height:103px;overflow:hidden}
.share{top:196px;width:35px;height:35px;border-radius:50%}
.date-day{top:1339px;width:99px;height:49px}
.date-day span,.date-mon span{position:absolute;right:14px;color:var(--white)}
.date-day span{font-size:40px;top:-2px;font-weight:300}
.date-mon{top:1397px;width:59px;height:30px;background:var(--dark)}
.date-mon span{font-size:14px;top:5px}

/* offer */
.offer-left{left:0;top:1600px;width:452px;height:200px;background:var(--blue)}
.offer-band{left:480px;top:1621px;width:870px;height:158px;background:var(--blue)}
.offer-kicker{left:99px;top:1652px;font-size:37px;color:var(--white)}
.offer-main{left:99px;top:1694px;font-size:48px;font-weight:600;color:var(--white)}
.train-title{left:523px;top:1650px;font-size:26px;color:var(--white)}
.email-box{left:527px;top:1697px;width:278px;height:44px;background:var(--white);font-size:13px;color:#888;padding:13px 16px}
.subscribe{left:805px;top:1697px;width:129px;height:44px;background:var(--dark);color:var(--white);font-size:13px;text-align:center;line-height:44px;letter-spacing:.4px}
.video{left:981px;top:1591px;width:270px;height:220px;background:#eee;border:1px solid #ccc;padding:5px}
.video-still{width:100%;height:100%;background:linear-gradient(180deg,#8fb4de 0%,#d6e1ee 45%,#2f63b8 55%,#9a9a9a 80%,#7f7f7f 100%)}

/* footer */
.foot-head{top:1855px;font-size:16px;font-weight:600;color:var(--ink);letter-spacing:.3px}
.foot-rule{top:1885px;width:265px;height:1px;background:var(--line)}
.foot-accent{top:1884px;width:38px;height:2px;background:var(--blue)}
.foot-text{font-size:13px;line-height:20px;color:var(--muted)}
.thumb{width:85px;height:64px}
.recent{left:674px;top:1907px;list-style:none}
.recent li{font-size:13px;color:var(--muted);height:29px;display:flex;align-items:center;gap:14px;padding-left:4px}
.recent li::before{content:"";width:6px;height:6px;border-top:1.5px solid var(--blue);border-right:1.5px solid var(--blue);transform:rotate(45deg)}
.info{left:961px;top:1907px;font-size:13px;color:var(--muted)}
.info div{height:25px;line-height:20px}
.info .k{display:inline-block;width:57px;color:var(--blue)}
.bottom{left:0;top:2089px;width:1350px;height:60px;background:var(--dark);color:var(--white);font-size:14px}
.bottom-links{right:100px;top:20px;display:flex;gap:20px}
</style>
</head>
<body>
<div class="page">

  <!-- header -->
  <div class="abs brand"><span class="brand-dot"></span><span class="brand-name">norvane</span></div>

  <div class="abs contact-item" style="left:873px;top:13px">
    <svg width="36" height="24" viewBox="0 0 36 24"><rect x="1" y="1" width="34" height="22" fill="none" stroke="#333" stroke-width="2"/><path d="M1 1 L18 14 L35 1 M1 23 L13 10 M35 23 L23 10" fill="none" stroke="#333" stroke-width="2"/></svg>
    <div><div class="contact-label">Email :</div><div class="contact-value">info@norvane.com</div></div>
  </div>
  <div class="abs contact-item" style="left:1050px;top:11px">
    <svg width="28" height="28" viewBox="0 0 24 24"><path fill="#0b78c4" d="M6.6 10.8c1.4 2.8 3.8 5.1 6.6 6.6l2.2-2.2c.3-.3.7-.4 1-.2 1.1.4 2.3.6 3.600.6.6 0 1 .4 1 1V20c0 .6-.4 1-1 1C10.6 21 3 13.4 3 4c0-.6.4-1 1-1h3.5c.6 0 1 .4 1 1 0 1.3.2 2.5.6 3.6.1.3 0 .7-.2 1L6.6 10.8z"/></svg>
    <div><div class="contact-label">Call Us :</div><div class="contact-value phone">(UK) +12-555-0142</div></div>
  </div>

  <!-- navigation -->
  <nav class="abs nav">
    <div class="abs nav-item active">Home</div>
    <div class="abs nav-item" style="left:214px">About Us</div>
    <div class="abs nav-item" style="left:323px">Product Category</div>
    <div class="abs nav-item" style="left:486px">Blog</div>
    <div class="abs nav-item" style="left:563px">Contact Us</div>
    <div class="abs search-sep"></div>
    <div class="abs search-text">search</div>
    <svg class="abs" style="left:1229px;top:17px" width="20" height="20" viewBox="0 0 20 20"><circle cx="8" cy="8" r="6" fill="none" stroke="#fff" stroke-width="2"/><path d="M12.5 12.5 L18 18" stroke="#fff" stroke-width="2.4"/></svg>
  </nav>

  <!-- hero -->
  <section class="abs hero" role="img" aria-label="Photo of tall silver industrial storage silos with blue metal stairways under a blue sky">
    <svg class="abs" style="left:0;top:0" width="1350" height="582" viewBox="0 0 1350 582">
      <path d="M0 0 H690 C800 60 810 250 700 390 C610 500 500 560 425 582 H0 Z" fill="#0b78c4" fill-opacity=".9"/>
    </svg>
    <h1 class="abs hero-title heading-font">Welcome To Norvane</h1>
    <p class="abs hero-text">Lorem ipsum dolor sit amet, consectetuer adipiscing elit. Aenean commodo ligula eget dolor aenean massa. Cum sociis natoque penatibus .</p>
    <div class="abs btn-more">Read More</div>

    <form class="abs request">
      <div class="abs request-title">SPECIAL REQUEST FORM</div>
      <div class="abs field" style="top:76px;height:50px">Name</div>
      <div class="abs field" style="top:133px;height:50px">Product</div>
      <div class="abs field" style="top:190px;height:166px">Message</div>
      <div class="abs submit">SUBMIT</div>
    </form>

    <span class="abs dot" style="left:649px"></span>
    <span class="abs dot on" style="left:669px"></span>
    <span class="abs dot" style="left:688px"></span>
  </section>

  <!-- product category -->
  <h2 class="abs section-title heading-font" style="top:736px;font-weight:400">Product Category</h2>
  <div class="abs rule" style="left:493px;top:791px;width:364px"></div>
  <div class="abs rule-accent" style="left:629px;top:790px;width:93px"></div>

  <div class="abs category" style="left:100px">
    <div class="category-photo" role="img" aria-label="Hands pouring liquid from a plastic bottle into a glass flask" style="background:linear-gradient(135deg,#8a8a8a 0%,#b9a89c 45%,#d3c6bc 60%,#6f6f73 100%)"></div>
    <div class="category-badge"><svg width="80" height="70" viewBox="0 0 80 70"><rect x="35" y="16" width="10" height="6" fill="#fff"/><path d="M33 24 H47 V44 a3 3 0 0 1 -3 3 H36 a3 3 0 0 1 -3 -3 Z" fill="#fff"/></svg></div>
    <div class="category-band"></div>
    <div class="category-label">PLASTIC</div>
  </div>
  <div class="abs category resin" style="left:490px">
    <div class="category-photo" role="img" aria-label="Close-up of an amber resin droplet on tree bark" style="background:linear-gradient(120deg,#4a3320 0%,#8c5a2a 35%,#e07a1a 55%,#6d4a3b 75%,#3a2a22 100%)"></div>
    <div class="category-badge"><svg width="80" height="70" viewBox="0 0 80 70"><path d="M40 16 C46 26 49 31 49 36 a9 9 0 0 1 -18 0 C31 31 34 26 40 16 Z" fill="#fff"/></svg></div>
    <div class="category-band"></div>
    <div class="category-label">RESIN</div>
  </div>
  <div class="abs category" style="left:880px">
    <div class="category-photo" role="img" aria-label="Industrial chemical plant with pipes and towers" style="background:linear-gradient(180deg,#a9bdd6 0%,#c3cfdc 45%,#8e8f8c 70%,#6a6d6a 100%)"></div>
    <div class="category-badge"><svg width="80" height="70" viewBox="0 0 80 70"><path d="M28 44 V30 L34 34 V30 L40 34 V30 L46 34 V22 H50 V44 Z" fill="#fff"/></svg></div>
    <div class="category-band"></div>
    <div class="category-label">INDUSTRIAL</div>
  </div>

  <!-- latest blog -->
  <h2 class="abs section-title heading-font" style="top:1141px;font-weight:400">Latest Blog</h2>
  <div class="abs rule" style="left:520px;top:1195px;width:310px"></div>
  <div class="abs rule-accent" style="left:629px;top:1194px;width:93px"></div>

  <div class="abs post-photo" style="left:99px" role="img" aria-label="Blue industrial valve and pipework in a processing plant">
    <div style="width:100%;height:100%;background:linear-gradient(135deg,#5d7fa8 0%,#2f63b0 40%,#b9c4cf 65%,#7d8793 100%)"></div>
  </div>
  <svg class="abs date-day" style="left:250px" viewBox="0 0 99 49"><path d="M20 0 H99 V49 H0 Z" fill="#0b78c4"/></svg>
  <div class="abs date-day" style="left:250px"><span>10</span></div>
  <div class="abs date-mon" style="left:290px"><span>AUG</span></div>
  <article class="abs post-card" style="left:349px">
    <h3 class="abs post-title heading-font" style="font-weight:400">Blog Heading 1</h3>
    <div class="abs post-mark"></div>
    <p class="abs post-text">Lorem ipsum dolor sit amet, consectetuer adipiscing elit. Aenean commodo ligula eget dolor. Cum sociis natoque penatibus et magnis Lorem ipsum dolor sit amet, consectetuer adipiscing elit.</p>
    <span class="abs share" style="left:35px;background:#3b5fa8"></span>
    <span class="abs share" style="left:77px;background:#2cc4f4"></span>
    <span class="abs share" style="left:118px;background:#e0261d"></span>
    <span class="abs share" style="left:159px;background:#1c4f88"></span>
  </article>

  <div class="abs post-photo" style="left:695px" role="img" aria-label="Rusted large pipes and ducts at an industrial site">
    <div style="width:100%;height:100%;background:linear-gradient(135deg,#9fb7cf 0%,#a36a4e 40%,#b98266 60%,#7f8fa0 100%)"></div>
  </div>
  <svg class="abs date-day" style="left:846px" viewBox="0 0 99 49"><path d="M20 0 H99 V49 H0 Z" fill="#0b78c4"/></svg>
  <div class="abs date-day" style="left:846px"><span>10</span></div>
  <div class="abs date-mon" style="left:886px"><span>AUG</span></div>
  <article class="abs post-card" style="left:945px">
    <h3 class="abs post-title heading-font" style="font-weight:400">Blog Heading 1</h3>
    <div class="abs post-mark"></div>
    <p class="abs post-text">Lorem ipsum dolor sit amet, consectetuer adipiscing elit. Aenean commodo ligula eget dolor. Cum sociis natoque penatibus et magnis Lorem ipsum dolor sit amet, consectetuer adipiscing elit.</p>
    <span class="abs share" style="left:35px;background:#3b5fa8"></span>
    <span class="abs share" style="left:77px;background:#2cc4f4"></span>
    <span class="abs share" style="left:118px;background:#e0261d"></span>
    <span class="abs share" style="left:159px;background:#1c4f88"></span>
  </article>

  <!-- special offer band -->
  <div class="abs offer-band"></div>
  <div class="abs offer-left"></div>
  <svg class="abs" style="left:452px;top:1600px" width="28" height="200" viewBox="0 0 28 200"><path d="M0 0 L28 21 V179 L0 200 Z" fill="#0a4f86"/></svg>
  <div class="abs offer-kicker heading-font">Advertising</div>
  <div class="abs offer-main heading-font">Special Offer</div>
  <div class="abs train-title heading-font">Train Your Employees</div>
  <div class="abs email-box">Email</div>
  <div class="abs subscribe">SUBCRIBE</div>
  <div class="abs video">
    <div class="video-still" role="img" aria-label="Video still of a warehouse building with blue cladding under a cloudy sky"></div>
    <svg class="abs" style="left:123px;top:97px" width="24" height="26" viewBox="0 0 24 26"><path d="M2 1 L22 13 L2 25 Z" fill="#fff"/></svg>
  </div>

  <!-- footer columns -->
  <div class="abs foot-head" style="left:99px">ABOUT US</div>
  <div class="abs foot-rule" style="left:99px"></div><div class="abs foot-accent" style="left:99px"></div>
  <p class="abs foot-text" style="left:98px;top:1902px;width:255px">Consectetuer adipiscing elit. Aenean commodo ligula eget dolor.</p>
  <p class="abs foot-text" style="left:100px;top:1948px;width:255px">consectetuer adipiscing elit. Aenean commodo ligula eget dolor. Aenean massa. Cum sociis natoque penatibus et magnis dis parturient montes.</p>

  <div class="abs foot-head" style="left:387px">GALLERY</div>
  <div class="abs foot-rule" style="left:387px"></div><div class="abs foot-accent" style="left:387px"></div>
  <div class="abs thumb" style="left:387px;top:1906px;background:linear-gradient(180deg,#7ea6d6,#2f63b8 60%,#c9c9c9)" role="img" aria-label="Warehouse building"></div>
  <div class="abs thumb" style="left:477px;top:1906px;background:linear-gradient(135deg,#3b3f44,#d9b43a 50%,#8a6a5a)" role="img" aria-label="Hands holding a multimeter"></div>
  <div class="abs thumb" style="left:567px;top:1906px;background:linear-gradient(180deg,#3d3a36,#a48d72 50%,#5a4d40)" role="img" aria-label="Factory hall interior"></div>
  <div class="abs thumb" style="left:387px;top:1976px;background:linear-gradient(135deg,#d9a441,#b0866a 40%,#707a84)" role="img" aria-label="Technician working on a panel"></div>
  <div class="abs thumb" style="left:477px;top:1976px;background:linear-gradient(135deg,#2c2a28,#8d5a3c 50%,#c76e2c)" role="img" aria-label="Machinery with glowing lights"></div>
  <div class="abs thumb" style="left:567px;top:1976px;background:radial-gradient(circle at 50% 45%,#d8d8d8 0,#9a9a9a 30%,#3f3a36 60%)" role="img" aria-label="Pressure gauge close-up"></div>

  <div class="abs foot-head" style="left:674px">RECENT POSTS</div>
  <div class="abs foot-rule" style="left:674px"></div><div class="abs foot-accent" style="left:674px"></div>
  <ul class="abs recent">
    <li>This is a Standard Post</li>
    <li>Post with Featured Image</li>
    <li>Beautiful Gallery Post</li>
    <li>This is a Video Post</li>
    <li>This is an Audio Post</li>
  </ul>

  <div class="abs foot-head" style="left:961px">CONTACT INFO</div>
  <div class="abs foot-rule" style="left:961px"></div><div class="abs foot-accent" style="left:961px"></div>
  <div class="abs info">
    <div>Unit 7/12 Harlow Street</div>
    <div>Norvane WA 06021</div>
    <div><span class="k">Phone:</span>(08) 5550 318</div>
    <div><span class="k">Fax:</span>(08) 5550 318</div>
    <div><span class="k">E-Mail:</span>info@norvane.com.au</div>
    <div><span class="k">Web:</span>http://www.norvane.com</div>
  </div>

  <footer class="abs bottom">
    <div class="abs" style="left:99px;top:20px">© 2016 &nbsp;| &nbsp;All Right Reserved</div>
    <div class="abs bottom-links"><span>Privacy Policy</span><span>Contact Us</span><span>Sitemap</span></div>
  </footer>

</div>
</body>
</html>
```